VORTAL Business Card Design

We need a business card for a new company based on the Gold Coast, we are a new supplement distributing company called VORTAL Sports Nutrition - Bold Horizon Sports Nutrition. We are providing new science based bodybuilding and fitness supplementation. Our company has a key focus towards next generation. We are wanting a card that is cool, innovative and fresh. We would like to see the implementation of the below image in a fresh and very innovative design that stands out. The final design should communicate New, Innovative, Cool, Science and researched based.
Target Market(s)
The target market is fitness and bodybuilder enthusiasts. Young audience so very cool looking.
Industry/Entity Type
Fitness
Contact Information for Business Card
(front of card)
VORTAL Sports Nutrition.
Liam Darrow
CEO/Sport Nutrition Specialist
0472 638 904
Liam@vortalsportsfuel.example
www.vortalsportsfuel.example
(back of card)
Scientifically formulated supplement range
Private Nutrition consultations
comprehensive sports nutrition seminars
Requirements
Nice to have
- The card could have a cut out on one of the sides or one of the corners rounded off so the card looks different from a normal business card.
Should not have
- The colours need to complement each other and pop out.

```html
<!DOCTYPE html>
<html lang="en">
<head>
<meta charset="utf-8">
<title>VORTAL Sports Nutrition – Business Card</title>
<link href="https://fonts.googleapis.com/css2?family=Questrial&display=swap" rel="stylesheet">
<style>
  :root {
    --backdrop-top: #8fa0ad;
    --backdrop-mid: #b7c4cd;
    --backdrop-edge: #7d8e9b;
    --card-fill: rgba(235, 242, 247, 0.45);
    --card-edge: rgba(255, 255, 255, 0.85);
    --band-fill: #f4f6f8;
    --accent-line: #6cc9ee;
    --brand-blue: #7fd0f3;
    --brand-faint: rgba(127, 208, 243, 0.55);
    --ink-blue: #1e8fc2;
    --ink-soft: #5cb8e0;
    --divider: #2a9bcc;
  }
  * { margin: 0; padding: 0; box-sizing: border-box; }
  html, body { width: 1200px; height: 792px; overflow: hidden; }
  body {
    position: relative;
    font-family: "Questrial", "Century Gothic", sans-serif;
    background: linear-gradient(90deg, var(--backdrop-edge) 0%, var(--backdrop-mid) 50%, var(--backdrop-edge) 100%);
  }
  .card {
    position: absolute;
    top: 232px;
    width: 518px;
    height: 333px;
    border-radius: 22px;
    background: var(--card-fill);
    border: 2px solid var(--card-edge);
    box-shadow: inset 0 0 18px rgba(255,255,255,0.5);
    overflow: hidden;
  }
  .card--front { left: 57px; }
  .card--back { left: 627px; }

  .brand {
    position: absolute;
    top: 60px;
    left: 0;
    right: 0;
    display: flex;
    flex-direction: column;
    align-items: center;
    gap: 14px;
  }
  .brand__dot {
    width: 88px;
    height: 88px;
    border-radius: 50%;
    background: var(--brand-blue);
  }
  .brand__name {
    font-size: 38px;
    letter-spacing: 3px;
    color: var(--brand-blue);
  }
  .card--back .brand__dot { background: var(--brand-faint); }
  .card--back .brand__name { color: var(--brand-faint); }

  .info-band {
    position: absolute;
    left: 0;
    right: 0;
    top: 210px;
    height: 80px;
    background: var(--band-fill);
    border-top: 3px solid var(--accent-line);
    border-bottom: 3px solid var(--accent-line);
  }

  .person {
    position: absolute;
    right: 307px;
    top: 20px;
    text-align: right;
  }
  .person__name { font-size: 19px; color: var(--ink-blue); font-weight: 700; }
  .person__role { font-size: 13px; color: var(--ink-soft); margin-top: 2px; }

  .band-divider {
    position: absolute;
    left: 228px;
    top: 10px;
    width: 2px;
    height: 56px;
    background: var(--divider);
  }

  .contacts {
    position: absolute;
    left: 244px;
    top: 10px;
    list-style: none;
  }
  .contacts li {
    display: flex;
    align-items: center;
    gap: 6px;
    font-size: 15px;
    line-height: 19px;
    color: var(--ink-blue);
  }
  .contacts svg { width: 15px; height: 15px; flex: none; }

  .services {
    position: absolute;
    inset: 0;
    display: flex;
    flex-direction: column;
    justify-content: center;
    align-items: center;
    font-size: 15px;
    line-height: 19px;
    color: var(--ink-blue);
  }
</style>
</head>
<body>
  <section class="card card--front" aria-label="Card front">
    <div class="brand">
      <span class="brand__dot"></span>
      <span class="brand__name">VORTAL</span>
    </div>
    <div class="info-band">
      <div class="person">
        <p class="person__name">Liam Darrow</p>
        <p class="person__role">CEO/Sport Nutrition Specialist</p>
      </div>
      <span class="band-divider"></span>
      <ul class="contacts">
        <li>
          <svg viewBox="0 0 16 16" aria-hidden="true"><path fill="#2a9bcc" d="M3.5 1.5l2.2 2.6-1.3 1.6c.9 2 2.4 3.5 4.4 4.4l1.6-1.3 2.6 2.2-1.4 2.3C6.8 13.1 2.9 9.2 1.2 4.4z"/></svg>
          0472 638 904
        </li>
        <li>
          <svg viewBox="0 0 16 16" aria-hidden="true" fill="none" stroke="#2a9bcc" stroke-width="1.2"><circle cx="8" cy="8" r="6.5"/><ellipse cx="8" cy="8" rx="3" ry="6.5"/><path d="M1.5 8h13M2.5 5h11M2.5 11h11"/></svg>
          www.vortalsportsfuel.example
        </li>
        <li>
          <svg viewBox="0 0 16 16" aria-hidden="true"><rect x="1" y="3.5" width="14" height="9.5" rx="1" fill="#2a9bcc"/><path d="M1.5 4.2L8 9l6.5-4.8" fill="none" stroke="#fff" stroke-width="1.2"/></svg>
          Liam@vortalsportsfuel.example
        </li>
      </ul>
    </div>
  </section>

  <section class="card card--back" aria-label="Card back">
    <div class="brand">
      <span class="brand__dot"></span>
      <span class="brand__name">VORTAL</span>
    </div>
    <div class="info-band">
      <div class="services">
        <p>Scientifically formulated supplement range</p>
        <p>Private Nutrition consultations</p>
        <p>comprehensive sports nutrition seminars</p>
      </div>
    </div>
  </section>
</body>
</html>
```